deceased estate clean ups brochures

we would like a brochure to reresent our business we already have new web site and want to do DL A4 brochure to give out to promote our business we already have logo www.brightvale.com.au is where you can get all info needed

Target Market(s)

families with loved ones that have past away
people done sizing or needing to decluter

Colors
cadf82
33b8a4
886aae
33a6d7

```html
<!DOCTYPE html>
<html lang="en">
<head>
<meta charset="utf-8">
<title>Brightvale – Deceased Estate Cleanups Brochure</title>
<link href="https://fonts.googleapis.com/css2?family=Open+Sans:wght@400;600;700;800&display=swap" rel="stylesheet">
<style>
  :root{
    --green:#4ea73e;
    --green-dark:#3b8b33;
    --green-deep:#2f7a2b;
    --lime:#cadf82;
    --lime-bright:#a6cf45;
    --ink:#3a3a3a;
    --ink-soft:#666;
    --paper:#ffffff;
    --stage:#e6e6e6;
  }
  *{box-sizing:border-box;margin:0;padding:0}
  html,body{width:1200px;height:2400px;overflow:hidden}
  body{background:var(--stage);font-family:"Open Sans",Arial,sans-serif;color:var(--ink);position:relative}

  .spread{position:absolute;left:50px;width:1100px;height:778px;display:grid;grid-template-columns:repeat(3,1fr);background:var(--paper);box-shadow:0 18px 40px rgba(0,0,0,.18)}
  .spread--outside{top:280px}
  .spread--inside{top:1340px}
  .panel{position:relative;overflow:hidden;height:100%}
  .panel + .panel{border-left:1px solid rgba(0,0,0,.06)}

  .photo{position:absolute;left:0;width:100%}
  .curve{position:absolute;left:0;width:100%;display:block}

  .heading{font-weight:800;text-transform:uppercase;letter-spacing:.3px}
  .rule{display:block;width:70px;height:3px;background:var(--lime-bright);margin:6px 0 0}

  /* brand name lockup */
  .brand{display:flex;align-items:center;gap:8px;justify-content:center}
  .brand__dot{width:16px;height:16px;border-radius:50%;background:var(--green)}
  .brand__name{font-weight:800;font-size:26px;letter-spacing:2px;color:var(--green-deep);text-transform:uppercase}

  /* steps panel */
  .steps{position:absolute;top:330px;left:34px;right:30px}
  .steps .heading{color:var(--green);font-size:17px}
  .step{display:flex;gap:10px;margin-top:20px}
  .step__num{font-size:34px;font-weight:800;color:var(--green);line-height:1;width:24px}
  .step__label{font-size:10px;font-weight:800;color:var(--green);letter-spacing:1px}
  .step__text{font-size:11px;line-height:1.45;color:var(--ink-soft)}

  /* contact panel */
  .panel--contact{background:var(--green);color:#fff;text-align:center}
  .badge{position:absolute;top:56px;left:50%;transform:translateX(-50%);width:150px;height:150px;border-radius:50%;background:#fff;border:6px solid var(--lime);display:flex;align-items:center;justify-content:center}
  .badge .brand__name{font-size:19px;letter-spacing:1px}
  .contact{position:absolute;top:250px;left:36px;right:36px}
  .contact .heading{font-size:22px}
  .contact__intro{font-size:12px;line-height:1.55;margin-top:14px}
  .socials{display:flex;gap:10px;justify-content:center;margin-top:22px}
  .socials span{width:22px;height:22px;border-radius:50%;border:1.5px solid #fff}
  .tagline{font-size:11px;font-weight:700;color:var(--lime);letter-spacing:1px;margin-top:26px}
  .phone-pill{display:inline-flex;align-items:center;gap:10px;background:var(--lime);color:var(--green-deep);font-weight:800;font-size:20px;letter-spacing:2px;padding:7px 26px;border-radius:24px;margin-top:10px}
  .phone-pill svg{width:16px;height:16px}
  .contact__details{font-size:13px;line-height:1.9;margin-top:16px}

  /* cover panel */
  .cover__brand{position:absolute;top:52px;left:0;right:0}
  .cover__text{position:absolute;top:600px;left:34px;right:30px}
  .cover__text .tagline{color:var(--green);margin-top:0;text-align:center}
  .cover__title{font-size:22px;font-weight:800;color:var(--ink);text-transform:uppercase;text-align:center;margin-top:4px}
  .cover__lead{font-size:12.5px;line-height:1.5;color:var(--ink-soft);margin-top:10px;text-align:center}

  /* about panel */
  .panel--about{background:var(--green);color:#fff}
  .about{position:absolute;top:372px;left:34px;right:30px}
  .about .heading{color:var(--lime);font-size:18px}
  .about p{font-size:11.5px;line-height:1.55;margin-top:10px}

  /* services panel */
  .services{padding:36px 30px 0}
  .services > .heading{color:var(--green);font-size:18px;text-align:center}
  .services > .rule{margin:6px auto 0}
  .service{display:flex;gap:12px;margin-top:15px;align-items:flex-start}
  .service__icon{flex:0 0 32px;height:32px;border-radius:50%;background:var(--green);display:flex;align-items:center;justify-content:center}
  .service__icon svg{width:16px;height:16px}
  .service__name{font-size:11.5px;font-weight:700;color:var(--ink)}
  .service__text{font-size:10px;line-height:1.45;color:var(--ink-soft)}
  .service-photos{display:flex;gap:6px;margin-top:16px}
  .service-photos div{flex:1;height:72px;border-radius:50%}
  .services .phone-pill{font-size:16px;padding:5px 22px;color:#fff;background:var(--green);margin:18px auto 0;display:flex;width:max-content}

  /* why panel */
  .why-bg{position:absolute;top:0;left:0;width:100%;height:470px;background:var(--green)}
  .why{position:absolute;top:36px;left:32px;right:28px;color:#fff}
  .why .heading{color:var(--lime);font-size:18px}
  .reason{display:flex;gap:10px;margin-top:18px}
  .reason svg{flex:0 0 16px;height:16px;margin-top:1px}
  .reason__name{font-size:12px;font-weight:700;color:var(--lime)}
  .reason__text{font-size:10.5px;line-height:1.45}
</style>
</head>
<body>

<!-- OUTSIDE SPREAD -->
<section class="spread spread--outside">

  <article class="panel panel--steps">
    <div class="photo" style="top:0;height:300px;background:linear-gradient(135deg,#d9c9a5,#7aa46a 55%,#f2e6b0)" role="img" aria-label="Photo of a cleaning team in aprons holding cleaning gear"></div>
    <svg class="curve" style="top:250px" viewBox="0 0 367 70" preserveAspectRatio="none" height="70">
      <path d="M0 40 Q180 -10 367 30 L367 70 L0 70Z" fill="var(--green)"/>
      <path d="M0 52 Q180 6 367 42 L367 70 L0 70Z" fill="#fff"/>
    </svg>
    <div class="steps">
      <h2 class="heading">Our 5 Step Process</h2><span class="rule"></span>
      <div class="step"><div class="step__num">1</div><div><div class="step__label">STEP</div><p class="step__text">Free on-site visit and a clear written quote for the whole property.</p></div></div>
      <div class="step"><div class="step__num">2</div><div><div class="step__label">STEP</div><p class="step__text">Items are sorted with the family, keeping what matters most.</p></div></div>
      <div class="step"><div class="step__num">3</div><div><div class="step__label">STEP</div><p class="step__text">Unwanted goods are removed, donated or recycled with care.</p></div></div>
      <div class="step"><div class="step__num">4</div><div><div class="step__label">STEP</div><p class="step__text">Repairs, cleaning and garden tidy-up are carried out.</p></div></div>
      <div class="step"><div class="step__num">5</div><div><div class="step__label">STEP</div><p class="step__text">The property is handed back spotless and ready for sale or rent.</p></div></div>
    </div>
  </article>

  <article class="panel panel--contact">
    <svg class="curve" style="top:0" viewBox="0 0 367 260" preserveAspectRatio="none" height="260">
      <path d="M0 0 L367 0 L367 120 Q200 220 0 150Z" fill="var(--green-dark)" opacity=".45"/>
    </svg>
    <div class="badge"><div class="brand"><span class="brand__name">Brightvale</span></div></div>
    <div class="contact">
      <h2 class="heading">Contact Us</h2>
      <p class="contact__intro">Welcome to Brightvale, a company that can gently ease your stress and take care of the estate of your loved one.</p>
      <div class="socials"><span></span><span></span><span></span><span></span></div>
      <p class="tagline">WE'RE HERE TO HELP</p>
      <div class="phone-pill">
        <svg viewBox="0 0 24 24"><path fill="currentColor" d="M6.6 10.8a15 15 0 0 0 6.6 6.6l2.2-2.2c.3-.3.7-.4 1-.2 1.1.4 2.3.6 3.6.6.6 0 1 .4 1 1V20c0 .6-.4 1-1 1A17 17 0 0 1 3 4c0-.6.4-1 1-1h3.5c.6 0 1 .4 1 1 0 1.3.2 2.5.6 3.6.1.3 0 .7-.2 1z"/></svg>
        0412 480 316
      </div>
      <p class="contact__details">PO Box 204, Ferndale 3099<br>info@brightvale.com.au<br>www.brightvale.com.au</p>
    </div>
  </article>

  <article class="panel panel--cover">
    <div class="cover__brand brand"><span class="brand__dot"></span><span class="brand__name">Brightvale</span></div>
    <svg class="curve" style="top:100px" viewBox="0 0 367 50" preserveAspectRatio="none" height="50">
      <path d="M0 50 Q200 -10 367 20 L367 50Z" fill="var(--lime-bright)"/>
      <path d="M0 50 Q200 8 367 34 L367 50Z" fill="var(--green)"/>
    </svg>
    <div class="photo" style="top:150px;height:420px;background:linear-gradient(160deg,#b7684a,#c98f6e 40%,#9fb6c9 70%,#e9e2d6)" role="img" aria-label="Photo of a smiling elderly couple sitting outside a brick home with a bucket of cleaning supplies"></div>
    <svg class="curve" style="top:530px" viewBox="0 0 367 60" preserveAspectRatio="none" height="60">
      <path d="M0 10 Q180 70 367 20 L367 60 L0 60Z" fill="var(--green)"/>
      <path d="M0 24 Q180 76 367 34 L367 60 L0 60Z" fill="#fff"/>
    </svg>
    <div class="cover__text">
      <p class="tagline">WE'RE HERE TO HELP</p>
      <h1 class="cover__title">Deceased Estate Cleanups</h1>
      <p class="cover__lead">At Brightvale our goal is to ease your worries and help you with your journey in preparing your house for rental or resale.</p>
    </div>
  </article>
</section>

<!-- INSIDE SPREAD -->
<section class="spread spread--inside">

  <article class="panel panel--about">
    <div class="photo" style="top:0;height:330px;background:linear-gradient(135deg,#f3efe8,#cfd6c9 50%,#a9b8a0)" role="img" aria-label="Photo of a consultant shaking hands with an older client at a table"></div>
    <svg class="curve" style="top:270px" viewBox="0 0 367 80" preserveAspectRatio="none" height="80">
      <path d="M0 20 Q190 80 367 10 L367 80 L0 80Z" fill="var(--lime-bright)"/>
      <path d="M0 34 Q190 92 367 24 L367 80 L0 80Z" fill="var(--green)"/>
    </svg>
    <div class="about">
      <h2 class="heading">About Our Company</h2>
      <p>At Brightvale our goal is to ease your worries, and help you with your journey in preparing your house for rental or resale.</p>
      <p>Whether it is a move to another residence or the difficult task of dealing with grief when a loved one passes away, Brightvale can help with the preparation of the property for sale. We will come in, remove unwanted items and dispose of all rubbish, do cosmetic repairs if required and leave the property in a spotless state.</p>
      <p>Our trained and reliable staff repair any house and carry out landscaping in preparation for renting or resale of the property in a timely and professional manner. Our team provides a discreet and trustworthy service, keeping in mind the sensitive nature of the work.</p>
    </div>
  </article>

  <article class="panel panel--services">
    <div class="services">
      <h2 class="heading">Services Offered</h2><span class="rule"></span>
      <div class="service"><div class="service__icon"><svg viewBox="0 0 24 24"><path fill="#fff" d="M12 3 2 12h3v8h5v-5h4v5h5v-8h3z"/></svg></div><div><p class="service__name">Senior / Aged Care Relocations and Downsizing</p><p class="service__text">Calm, careful help moving into a smaller home or aged care.</p></div></div>
      <div class="service"><div class="service__icon"><svg viewBox="0 0 24 24"><path fill="#fff" d="M12 3 2 12h3v8h5v-5h4v5h5v-8h3z"/></svg></div><div><p class="service__name">Deceased Estates</p><p class="service__text">Respectful clearing and sorting of a loved one's home and belongings.</p></div></div>
      <div class="service"><div class="service__icon"><svg viewBox="0 0 24 24"><path fill="#fff" d="M20 6 9 17l-5-5 1.4-1.4L9 14.2 18.6 4.6z"/></svg></div><div><p class="service__name">Cleaning Service</p><p class="service__text">Thorough top-to-bottom cleaning of every room, inside and out.</p></div></div>
      <div class="service-photos">
        <div style="background:linear-gradient(135deg,#d8d2c4,#9a8e7c)" role="img" aria-label="Photo of packed moving boxes"></div>
        <div style="background:linear-gradient(135deg,#8e8a86,#c9c2b8)" role="img" aria-label="Photo of a house exterior"></div>
        <div style="background:linear-gradient(135deg,#e4ddd2,#a39583)" role="img" aria-label="Photo of a cleared living room"></div>
      </div>
      <div class="service"><div class="service__icon"><svg viewBox="0 0 24 24"><path fill="#fff" d="M12 3 2 12h3v8h5v-5h4v5h5v-8h3z"/></svg></div><div><p class="service__name">Cosmetic Repairs and House Maintenance</p><p class="service__text">Patching, painting and small fixes to present the home well.</p></div></div>
      <div class="service"><div class="service__icon"><svg viewBox="0 0 24 24"><path fill="#fff" d="M12 3 2 12h3v8h5v-5h4v5h5v-8h3z"/></svg></div><div><p class="service__name">Preparation for Rental or Sale</p><p class="service__text">Getting the property ready for inspections and listing photos.</p></div></div>
      <div class="service"><div class="service__icon"><svg viewBox="0 0 24 24"><path fill="#fff" d="M20 6 9 17l-5-5 1.4-1.4L9 14.2 18.6 4.6z"/></svg></div><div><p class="service__name">Garden Makeovers</p><p class="service__text">Mowing, pruning and tidy-ups for a fresh first impression.</p></div></div>
      <div class="phone-pill">
        <svg viewBox="0 0 24 24"><path fill="currentColor" d="M6.6 10.8a15 15 0 0 0 6.6 6.6l2.2-2.2c.3-.3.7-.4 1-.2 1.1.4 2.3.6 3.6.6.6 0 1 .4 1 1V20c0 .6-.4 1-1 1A17 17 0 0 1 3 4c0-.6.4-1 1-1h3.5c.6 0 1 .4 1 1 0 1.3.2 2.5.6 3.6.1.3 0 .7-.2 1z"/></svg>
        0412 480 316
      </div>
    </div>
  </article>

  <article class="panel panel--why">
    <div class="why-bg"></div>
    <svg class="curve" style="top:430px" viewBox="0 0 367 80" preserveAspectRatio="none" height="80">
      <path d="M0 0 L367 0 L367 30 Q180 90 0 40Z" fill="var(--green)"/>
      <path d="M0 40 Q180 90 367 30 L367 44 Q180 104 0 54Z" fill="var(--lime-bright)"/>
    </svg>
    <div class="photo" style="top:500px;height:278px;background:linear-gradient(135deg,#eef0ea,#d9dfc9 50%,#f0d36a)" role="img" aria-label="Photo of cleaners in aprons wiping a table and mopping a bright room"></div>
    <div class="why">
      <h2 class="heading">Why Choose Us?</h2><span class="rule"></span>
      <div class="reason"><svg viewBox="0 0 24 24"><path fill="var(--lime)" d="M20 6 9 17l-5-5 1.4-1.4L9 14.2 18.6 4.6z"/></svg><div><p class="reason__name">Trusted</p><p class="reason__text">A caring local team that treats every home as if it were our own family's.</p></div></div>
      <div class="reason"><svg viewBox="0 0 24 24"><path fill="var(--lime)" d="M20 6 9 17l-5-5 1.4-1.4L9 14.2 18.6 4.6z"/></svg><div><p class="reason__name">Professional</p><p class="reason__text">Fully insured staff who work quickly, tidily and to an agreed timeline.</p></div></div>
      <div class="reason"><svg viewBox="0 0 24 24"><path fill="var(--lime)" d="M20 6 9 17l-5-5 1.4-1.4L9 14.2 18.6 4.6z"/></svg><div><p class="reason__name">Caring</p><p class="reason__text">We listen first and move at a pace that suits you and your family.</p></div></div>
      <div class="reason"><svg viewBox="0 0 24 24"><path fill="var(--lime)" d="M20 6 9 17l-5-5 1.4-1.4L9 14.2 18.6 4.6z"/></svg><div><p class="reason__name">One Service</p><p class="reason__text">Cleaning, repairs, rubbish removal and gardens handled under one roof.</p></div></div>
    </div>
  </article>
</section>

</body>
</html>
```